HVAC contracting company needs a mordern business card!

We need a business card design for our Air condition company based in UAE since 1988. We specialize in the installation, maintenance of Air-condition equipments for both residential & commercial projects. We would like to have a card design that is modern.The card design should be relevant to our work.

Target Market(s)

MNCs, local house owners

Industry/Entity Type

Hvac

Contact Information for Business Card

Tel : +971 9 5614082, +971 9 5614093
Fax : +971 9 5614071
Mobile : +971 50 7361524
PO. Box : 382, Fujairah, U.A.E
Email : info@kbrzephyr.example
Website : www.kbrcooling.example

Requirements
Must have
• - Include all contact details & company logos
• - include the logos of the brands that we support
Nice to have
• Since most of our clients are arabic speak/arab origins, arabic translation of the business card would great to have!
Should not have
• Dark colors/background

```html
<!DOCTYPE html>
<html lang="en">
<head>
<meta charset="utf-8">
<title>KBR Zephyr Cooling Co. – Business Card</title>
<link rel="stylesheet" href="https://fonts.googleapis.com/css2?family=Lato:wght@400;700&display=swap">
<style>
  :root {
    --page-bg: #e8ecef;
    --card-bg: #ffffff;
    --card-edge: #d5dade;
    --brand-red: #ec1c24;
    --band-grey: #58585a;
    --ink: #1d1d1d;
    --faint: #dcdcdc;
    --white: #ffffff;
  }
  * { box-sizing: border-box; margin: 0; padding: 0; }
  html, body {
    width: 1200px; height: 1000px; overflow: hidden;
    background: var(--page-bg);
    font-family: "Lato", Arial, sans-serif;
    color: var(--ink);
  }
  .canvas { position: relative; width: 1200px; height: 1000px; }

  .card {
    position: absolute;
    background: var(--card-bg);
    border: 1px solid var(--card-edge);
    overflow: hidden;
  }
  .card--front { left: 302px; top: 145px; width: 596px; height: 332px; }
  .card--back  { left: 302px; top: 521px; width: 595px; height: 331px; }

  /* Front */
  .brand-mark {
    position: absolute; left: 24px; top: 96px; width: 164px; height: 148px;
    display: flex; flex-direction: column; align-items: center; justify-content: center; gap: 10px;
  }
  .brand-mark__dot {
    width: 22px; height: 22px; border-radius: 50%; background: var(--brand-red);
  }
  .brand-mark__name {
    font-size: 26px; font-weight: 700; color: var(--brand-red); letter-spacing: 0.5px;
  }
  .services {
    position: absolute; left: 212px; top: 101px; list-style: none;
  }
  .services li {
    position: relative; padding-left: 12px;
    font-size: 15px; line-height: 20px; height: 35px;
  }
  .services li::before {
    content: ""; position: absolute; left: 0; top: 8px;
    width: 6px; height: 6px; border-radius: 50%; background: var(--brand-red);
  }

  /* Back */
  .watermark {
    position: absolute; left: 150px; top: 230px;
    font-size: 26px; font-weight: 400; color: var(--faint);
  }
  .name-band {
    position: absolute; left: 0; top: 94px; width: 301px; height: 97px;
    background: var(--band-grey); color: var(--white);
    text-align: right; padding: 24px 28px 0 0;
  }
  .name-band__name { font-size: 22px; font-weight: 700; line-height: 26px; }
  .name-band__title { font-size: 20px; line-height: 28px; }
  .company-band {
    position: absolute; left: 0; top: 201px; width: 301px; height: 36px;
    background: var(--brand-red); color: var(--white);
    text-align: right; padding-right: 28px;
    font-size: 16px; line-height: 36px;
  }
  .contacts { position: absolute; left: 334px; top: 38px; list-style: none; }
  .contacts li { display: flex; align-items: flex-start; margin-bottom: 23px; }
  .contacts__icon { width: 14px; height: 14px; margin-top: 4px; margin-right: 9px; flex: none; }
  .contacts__icon svg { width: 14px; height: 14px; fill: var(--brand-red); display: block; }
  .contacts__text { font-size: 18px; line-height: 23px; }
  .contacts__row { display: flex; }
</style>
</head>
<body>
<main class="canvas">

  <section class="card card--front" aria-label="Card front">
    <div class="brand-mark">
      <span class="brand-mark__dot"></span>
      <span class="brand-mark__name">KBR Zephyr</span>
    </div>
    <ul class="services">
      <li>Maintainance &amp; Installation Of Lifts</li>
      <li>Maintainance &amp; Installation Of Central &amp; Split A.C.</li>
      <li>Installation Of False Ceilling &amp; Partitions</li>
      <li>Building Maintainance</li>
    </ul>
  </section>

  <section class="card card--back" aria-label="Card back">
    <span class="watermark">KBR Zephyr</span>

    <div class="name-band">
      <p class="name-band__name">DANIEL K. VARGHESE</p>
      <p class="name-band__title">Managing Partner</p>
    </div>
    <div class="company-band">KBR ZEPHYR COOLING CO.</div>

    <ul class="contacts">
      <li>
        <span class="contacts__icon"><svg viewBox="0 0 14 14"><path d="M7 0a4.5 4.5 0 0 0-4.5 4.5C2.5 8 7 14 7 14s4.5-6 4.5-9.5A4.5 4.5 0 0 0 7 0zm0 6.3a1.8 1.8 0 1 1 0-3.6 1.8 1.8 0 0 1 0 3.6z"/></svg></span>
        <span class="contacts__text">PO. Box: 382<br>Fujairah, U.A.E.</span>
      </li>
      <li>
        <span class="contacts__icon"><svg viewBox="0 0 14 14"><path d="M3 1l2.2 2.6-1.2 1.6c.8 1.8 2.1 3.1 3.9 3.9l1.6-1.2L12 10.1 10.6 12.5C6 12 2 8 1.5 3.4z"/></svg></span>
        <span class="contacts__text">+971 9 5614082<br>+971 9 5614093</span>
      </li>
      <li>
        <span class="contacts__icon"><svg viewBox="0 0 14 14"><path d="M1 5h12v8H1zM3 1h6v3H3zM3 7h2v1.5H3zm3 0h2v1.5H6zm3 0h2v1.5H9zM3 10h2v1.5H3zm3 0h2v1.5H6zm3 0h2v1.5H9z"/></svg><svg viewBox="0 0 14 14" style="margin-top:9px"><path d="M4 0h6a1 1 0 0 1 1 1v12a1 1 0 0 1-1 1H4a1 1 0 0 1-1-1V1a1 1 0 0 1 1-1zm.5 1.5v9.5h5V1.5z"/></svg></span>
        <span class="contacts__text">+971 9 5614071<br>+971 50 7361524</span>
      </li>
      <li>
        <span class="contacts__icon"><svg viewBox="0 0 14 14"><path d="M0 3h14v1L7 8.5 0 4zm0 2.4l7 4.4 7-4.4V12H0z"/></svg><svg viewBox="0 0 14 14" style="margin-top:9px"><path d="M1 2h12v8H8v1.5h2V13H4v-1.5h2V10H1zm1.5 1.5v5h9v-5z"/></svg></span>
        <span class="contacts__text">info@kbrzephyr.example<br>www.kbrcooling.example</span>
      </li>
    </ul>
  </section>

</main>
</body>
</html>
```